Business Card & Logo

Business Card Design Project & Logo

Need logo for business card

Company name is ZORVA

Target Market(s)

Consumer

Industry/Entity Type

Sporting Good

Contact Information for Business Card

Electric Bike Business Cards, Flyers, and LOGO.

Font styles to use
Sans Serif

Colors
ffc214
ffcf3e
faa54b
fee18a
f37122

Requirements
Must have
• New look &LOGO

```html
<!DOCTYPE html>
<html lang="en">
<head>
<meta charset="utf-8">
<title>ZORVA – Business Card</title>
<link href="https://fonts.googleapis.com/css2?family=Exo+2:wght@700&family=Open+Sans:wght@400;600&display=swap" rel="stylesheet">
<style>
  :root {
    --page: #e4e4e4;
    --card: #262626;
    --orange: #f37122;
    --yellow: #ffc214;
    --text: #f2f2f2;
    --muted: #e0e0e0;
  }
  * { margin: 0; padding: 0; box-sizing: border-box; }
  html, body { width: 1200px; height: 576px; overflow: hidden; }
  body {
    position: relative;
    background: var(--page);
    font-family: "Open Sans", Arial, sans-serif;
  }
  .card {
    position: absolute;
    background: var(--card);
    border-radius: 12px;
    box-shadow: 0 3px 6px rgba(0,0,0,0.28);
  }
  .card-front { left: 82px; top: 139px; width: 484px; height: 293px; }
  .card-back  { left: 602px; top: 138px; width: 481px; height: 291px; }

  .brand {
    position: absolute;
    display: flex;
    align-items: center;
    gap: 12px;
    color: var(--yellow);
    font-family: "Open Sans", Arial, sans-serif;
    font-weight: 600;
    line-height: 1;
    letter-spacing: 3px;
  }
  .brand-dot {
    width: 12px; height: 12px; border-radius: 50%;
    background: var(--yellow);
    flex: none;
  }
  .card-front .brand {
    left: 50%; top: 122px;
    transform: translateX(-50%);
    font-size: 44px;
  }
  .card-back .brand {
    left: 62px; top: 130px;
    font-size: 32px;
    gap: 10px;
  }
  .card-back .brand-dot { width: 10px; height: 10px; }

  .contact { position: absolute; left: 247px; top: 84px; color: var(--text); }
  .person-name {
    font-family: "Exo 2", Arial, sans-serif;
    font-weight: 700;
    font-size: 20px;
    color: var(--orange);
    line-height: 1;
  }
  .person-role { font-size: 11px; color: var(--muted); margin-top: 6px; }
  .contact-list { list-style: none; margin-top: 14px; }
  .contact-list li {
    display: flex; align-items: center;
    font-size: 11.5px; height: 16.5px; color: var(--text);
  }
  .contact-list svg { width: 11px; height: 11px; margin-right: 13px; fill: var(--orange); }
  .address { font-size: 11.5px; margin-top: 3px; color: var(--text); }
</style>
</head>
<body>
  <section class="card card-front" aria-label="Card front">
    <div class="brand">
      <span class="brand-dot"></span>
      <span class="brand-name">ZORVA</span>
    </div>
  </section>

  <section class="card card-back" aria-label="Card back">
    <div class="brand">
      <span class="brand-dot"></span>
      <span class="brand-name">ZORVA</span>
    </div>
    <div class="contact">
      <p class="person-name">Daniel Reyes</p>
      <p class="person-role">Founder/Director</p>
      <ul class="contact-list">
        <li><svg viewBox="0 0 12 12" aria-hidden="true"><path d="M1 3 Q6 0 11 3 L10 5 L8 4 L8 3 Q6 2 4 3 L4 4 L2 5 Z M3 6 H9 L10 11 H2 Z"/></svg>12-555-0142</li>
        <li><svg viewBox="0 0 12 12" aria-hidden="true"><path d="M3 0 H9 V12 H3 Z M4 1.5 V9.5 H8 V1.5 Z"/></svg>daniel.reyes@zorvabikes.com</li>
        <li><svg viewBox="0 0 12 12" aria-hidden="true"><path d="M3 0 H9 V3 H3 Z M0 4 H12 V9 H10 V7 H2 V9 H0 Z M3 8 H9 V12 H3 Z"/></svg>www.zorvabikes.com</li>
      </ul>
      <p class="address">48 Harbour Lane No.7, Sydney 2000</p>
    </div>
  </section>
</body>
</html>
```